Website for Excavator and Earthworks Company

We require a modern, sleek and practical website for our newly created earthworks/excavator business in Perth, Western Australia called Gullwind Stonecut Earthworks.

The website should have a modern, cutting edge feel but only needs to be relatively simplistic in it's layout and eventual functionality.

Some pages it should have would be Home, About, Projects and Contact Us.

Number of Pages Required

1 page

```html
<!DOCTYPE html>
<html lang="en">
<head>
<meta charset="utf-8">
<title>Gullwind Stonecut Earthworks</title>
<link href="https://fonts.googleapis.com/css2?family=Montserrat:wght@400;500;600;700;800&display=swap" rel="stylesheet">
<style>
:root{
  --lime:#c8e600;
  --ink:#0f0f0f;
  --panel:#1b1b1b;
  --field:#2a2a2a;
  --white:#ffffff;
  --grey:#6b6b6b;
  --light:#f4f4f4;
}
*{margin:0;padding:0;box-sizing:border-box}
html,body{width:1200px;height:3792px;overflow:hidden}
body{font-family:'Montserrat',sans-serif;color:var(--ink);background:var(--white);position:relative}
.abs{position:absolute}
.btn{position:absolute;display:flex;align-items:center;gap:14px;background:var(--lime);color:var(--ink);font-weight:700;font-size:13px;letter-spacing:.5px;text-transform:uppercase;padding:0 22px;height:40px;white-space:nowrap}
.btn .mark{width:14px;height:14px;background:var(--ink)}
.brand{position:absolute;display:flex;align-items:center;gap:12px;font-weight:800;color:var(--white);text-transform:uppercase}
.brand .sq{background:var(--lime)}
.label{position:absolute;font-size:12px;font-weight:700;color:var(--lime);letter-spacing:1px;text-transform:uppercase;display:flex;align-items:center;gap:10px}
.label::before{content:"";width:40px;height:2px;background:var(--lime)}
.h2{position:absolute;font-weight:800;text-transform:uppercase;line-height:1.12}

/* hero */
.hero{position:absolute;left:0;top:0;width:1200px;height:784px;background:linear-gradient(180deg,#3b2a1c 0%,#a0612a 35%,#5a3b22 65%,#1a130e 100%)}
.hero-shade{position:absolute;inset:0;background:linear-gradient(90deg,rgba(0,0,0,.55),rgba(0,0,0,.1))}
.nav-links{position:absolute;left:632px;top:48px;display:flex;gap:26px;color:var(--white);font-size:13px;font-weight:500}
.hero-title{position:absolute;left:148px;top:492px;color:var(--white);font-size:44px;font-weight:800;line-height:1.15;text-transform:uppercase}
.hero-lede{position:absolute;left:488px;top:496px;width:250px;color:var(--white);font-size:12px;line-height:1.5}
.hero-dots{position:absolute;left:148px;top:716px;display:flex;gap:8px}
.hero-dots i{width:8px;height:8px;border-radius:50%;background:rgba(255,255,255,.5)}
.hero-dots i:first-child{background:var(--white)}

/* about */
.about-copy{position:absolute;left:120px;top:1060px;width:330px;font-size:13px;line-height:1.65;color:var(--grey)}
.about-copy h3{font-size:15px;color:var(--ink);font-weight:800;margin-bottom:18px;text-transform:uppercase}
.about-copy p{margin-bottom:16px}
.about-photo{position:absolute;left:520px;top:1060px;width:560px;height:372px;background:linear-gradient(160deg,#8fb3d4 0%,#c7a36a 45%,#a47a45 100%)}
.value-box{position:absolute;padding:22px 18px;font-size:11px;line-height:1.5}
.value-box h4{font-size:15px;font-weight:800;text-transform:uppercase;line-height:1.2;margin-bottom:10px}
.mission{left:732px;top:1000px;width:140px;height:168px;background:var(--ink);color:var(--white)}
.vision{left:896px;top:1000px;width:144px;height:140px;background:var(--lime);color:var(--ink)}

/* video */
.video{position:absolute;left:0;top:1568px;width:1200px;height:260px;background:linear-gradient(90deg,#2e2418 0%,#6f5a42 45%,#8d7660 75%,#4a3c2c 100%)}
.video-title{position:absolute;left:0;right:0;top:112px;text-align:center;font-size:38px;font-weight:800;color:rgba(255,255,255,.55);text-transform:uppercase}

/* projects */
.card{position:absolute;top:2060px;width:432px;height:420px;background:var(--panel);overflow:hidden}
.card-photo{height:250px}
.card-body{padding:18px 22px;color:var(--white)}
.card-body h4{font-size:15px;font-weight:800;text-transform:uppercase;margin-bottom:10px}
.card-body p{font-size:12px;line-height:1.55;color:#cfcfcf;width:300px}
.card-arrow{position:absolute;right:20px;bottom:20px;width:44px;height:44px;background:var(--lime);display:flex;align-items:center;justify-content:center}
.slider{position:absolute;left:520px;top:2502px;display:flex;gap:6px}
.slider i{width:40px;height:3px;background:#d5d5d5}
.slider i:first-child{background:var(--ink)}

/* contact cta */
.cta-bg{position:absolute;left:0;top:2560px;width:1200px;height:640px;background:var(--light)}
.form{position:absolute;left:120px;top:2620px;width:488px;height:508px;background:var(--ink);padding:40px 40px}
.field{height:44px;background:var(--field);color:#bdbdbd;font-size:13px;display:flex;align-items:center;padding:0 16px;margin-bottom:14px}
.field.msg{height:96px;align-items:flex-start;padding-top:14px}
.cta-copy{position:absolute;left:688px;top:2906px;width:390px;font-size:13px;line-height:1.6;color:var(--grey)}

/* stats */
.stat{position:absolute;top:3232px;display:flex;align-items:center;gap:14px}
.stat b{display:block;font-size:30px;font-weight:800;line-height:1}
.stat span{font-size:12px;color:var(--grey)}

/* footer */
.footer{position:absolute;left:0;top:3392px;width:1200px;height:400px;background:var(--ink);color:var(--white)}
.f-col{position:absolute;top:80px;font-size:13px;line-height:2}
.f-col h5{font-size:14px;font-weight:800;text-transform:uppercase;margin-bottom:8px}
.contact-row{display:flex;gap:12px;align-items:flex-start;line-height:1.5;margin-bottom:18px}
.contact-row .ic{width:32px;height:32px;border-radius:50%;background:var(--lime);flex:none;display:flex;align-items:center;justify-content:center}
.newsletter{position:absolute;left:888px;top:88px;width:252px;height:124px;background:var(--lime);color:var(--ink);padding:22px 20px}
.newsletter h5{font-size:14px;font-weight:800;text-transform:uppercase;margin-bottom:16px}
.nl-input{display:flex;height:36px;background:var(--white)}
.nl-input span{flex:1;font-size:11px;color:#888;display:flex;align-items:center;padding-left:12px}
.nl-input i{width:36px;background:var(--ink)}
.socials{position:absolute;left:1028px;top:256px;display:flex;gap:10px}
.socials i{width:32px;height:32px;border-radius:50%;border:1px solid #555}
.f-rule{position:absolute;left:80px;right:60px;top:316px;height:1px;background:#2e2e2e}
.copyright{position:absolute;left:80px;top:344px;font-size:12px;color:#9a9a9a}
</style>
</head>
<body>

<header class="hero">
  <div role="img" aria-label="Excavator digging at sunset on a construction site" class="abs" style="inset:0"></div>
  <div class="hero-shade"></div>
  <div class="brand" style="left:96px;top:40px;font-size:17px"><span class="sq" style="width:28px;height:28px"></span>Gullwind Stonecut Earthworks</div>
  <nav class="nav-links"><span>Home</span><span>About</span><span>Projects</span><span>Contact</span></nav>
  <div class="btn" style="left:916px;top:36px;height:38px;font-size:12px">Get a Quote</div>
  <p class="hero-lede">Professional Earthworks &amp; Excavation Services in Perth, <b>Western Australia</b></p>
  <h1 class="hero-title">Raising the<br>ground. Building<br>the future.</h1>
  <div class="btn" style="left:812px;top:548px"><span class="mark"></span>View Our Projects</div>
  <div class="hero-dots"><i></i><i></i><i></i></div>
</header>

<section class="about">
  <div class="label" style="left:120px;top:924px">What We Do</div>
  <h2 class="h2" style="left:384px;top:868px;font-size:36px">Reliable earthworks you<br>can trust</h2>
  <div class="about-copy">
    <h3>Gullwind Stonecut Earthworks</h3>
    <p>Gullwind Stonecut Earthworks delivers high quality excavation and earthmoving services across Perth and surrounding areas. We work with builders, developers and private clients to prepare sites efficiently, safely and to the highest standards.</p>
    <p>With modern machinery, skilled operators and a commitment to precision, we make sure your project starts on solid ground.</p>
  </div>
  <div class="btn" style="left:120px;top:1312px"><span class="mark"></span>View Our Projects</div>
  <div class="about-photo" role="img" aria-label="Yellow excavator working beside site cabins under a blue sky"></div>
  <div class="value-box mission"><h4>Our<br>Mission</h4>To bring fast, reliable site works delivered on time.</div>
  <div class="value-box vision"><h4>Our<br>Vision</h4>To be Perth's most trusted earthworks team.</div>
</section>

<section class="video" role="img" aria-label="Excavator and worker on a sandy site, video preview">
  <div class="video-title">Watch Our Video</div>
</section>

<section class="projects">
  <div class="label" style="left:120px;top:1840px">Projects</div>
  <h2 class="h2" style="left:120px;top:1872px;font-size:36px">Transforming Perth, one<br>project at a time</h2>
  <div class="btn" style="left:832px;top:1944px"><span class="mark"></span>View All Projects</div>

  <article class="card" style="left:88px">
    <div class="card-photo" role="img" aria-label="Excavator digging on a cleared lot" style="background:linear-gradient(160deg,#9a9a96,#6d675c 60%,#3a342c)"></div>
    <div class="card-body"><h4>Some Goes Project Here</h4><p>With modern machinery, skilled operators, and a commitment to precision, we make sure your project starts on solid ground.</p></div>
    <div class="card-arrow"><svg width="18" height="14" viewBox="0 0 18 14"><path d="M0 7h15M10 1l6 6-6 6" stroke="#0f0f0f" stroke-width="2.4" fill="none"/></svg></div>
  </article>
  <article class="card" style="left:532px">
    <div class="card-photo" role="img" aria-label="Orange excavator trenching in red soil" style="background:linear-gradient(160deg,#b0653a,#7a4528 55%,#3c2416)"></div>
    <div class="card-body"><h4>Some Goes Project Here</h4><p>With modern machinery, skilled operators, and a commitment to precision, we make sure your project starts on solid ground.</p></div>
    <div class="card-arrow"><svg width="18" height="14" viewBox="0 0 18 14"><path d="M0 7h15M10 1l6 6-6 6" stroke="#0f0f0f" stroke-width="2.4" fill="none"/></svg></div>
  </article>
  <article class="card" style="left:972px">
    <div class="card-photo" role="img" aria-label="Excavator loading soil at dusk" style="background:linear-gradient(160deg,#8b7b70,#a05a36 55%,#40281a)"></div>
    <div class="card-body"><h4>Some Goes Project Here</h4><p>With modern machinery, skilled operators, and a commitment to precision, we make sure your project starts on solid ground.</p></div>
  </article>
  <div class="slider"><i></i><i></i><i></i></div>
</section>

<section class="cta">
  <div class="cta-bg"></div>
  <form class="form">
    <div class="field">First Name</div>
    <div class="field">Last Name</div>
    <div class="field">Email Address</div>
    <div class="field">Phone Number</div>
    <div class="field msg">Message</div>
  </form>
  <div class="btn" style="left:230px;top:3072px"><span class="mark"></span>Make an Appointment</div>
  <h2 class="h2" style="left:688px;top:2812px;font-size:38px">Ready to<br>get started?</h2>
  <p class="cta-copy">Whether you're planning a new build or need professional excavation services, Gullwind Stonecut Earthworks is here to help. Get in touch today for a fast, reliable quote.</p>
  <div class="btn" style="left:688px;top:3004px"><span class="mark"></span>Get a Quote</div>
</section>

<section class="stats">
  <div class="stat" style="left:100px"><svg width="40" height="40" viewBox="0 0 40 40"><circle cx="20" cy="20" r="17" fill="none" stroke="#0f0f0f" stroke-width="2"/><path d="M13 21l5 5 9-11" stroke="#0f0f0f" stroke-width="2.4" fill="none"/></svg><div><b>652K+</b><span>Client Satisfaction</span></div></div>
  <div class="stat" style="left:380px"><svg width="40" height="40" viewBox="0 0 40 40"><circle cx="20" cy="20" r="17" fill="none" stroke="#0f0f0f" stroke-width="2"/><circle cx="20" cy="18" r="6" fill="none" stroke="#0f0f0f" stroke-width="2"/><path d="M16 23l-2 8 6-3 6 3-2-8" stroke="#0f0f0f" stroke-width="2" fill="none"/></svg><div><b>2863+</b><span>Worldwide Awards</span></div></div>
  <div class="stat" style="left:660px"><svg width="40" height="40" viewBox="0 0 40 40"><rect x="6" y="6" width="28" height="28" fill="none" stroke="#0f0f0f" stroke-width="2"/><path d="M11 27l7-7 5 4 7-9" stroke="#0f0f0f" stroke-width="2" fill="none"/></svg><div><b>878%</b><span>Project Investment</span></div></div>
  <div class="stat" style="left:920px"><svg width="40" height="40" viewBox="0 0 40 40"><path d="M8 32V18M16 32V12M24 32V20M32 32V8" stroke="#0f0f0f" stroke-width="3"/></svg><div><b>856%</b><span>Business Growing</span></div></div>
</section>

<footer class="footer">
  <div class="brand" style="left:80px;top:96px;font-size:20px;width:300px;line-height:1.25"><span class="sq" style="width:40px;height:40px;flex:none"></span>Gullwind Stonecut Earthworks</div>
  <div class="f-col" style="left:448px"><h5>Quick Links</h5>Home<br>About<br>Projects<br>Contact Us</div>
  <div class="f-col" style="left:628px"><h5>Contact Us</h5>
    <div class="contact-row"><span class="ic"><svg width="14" height="14" viewBox="0 0 14 14"><path d="M2 1h3l1 3-2 1a8 8 0 0 0 4 4l1-2 3 1v3a1 1 0 0 1-1 1A11 11 0 0 1 1 2a1 1 0 0 1 1-1z" fill="#0f0f0f"/></svg></span><div><b>Call Us Today</b><br>0400 123 456</div></div>
    <div class="contact-row"><span class="ic"><svg width="14" height="12" viewBox="0 0 14 12"><rect x="1" y="1" width="12" height="10" fill="none" stroke="#0f0f0f" stroke-width="1.6"/><path d="M1 1l6 5 6-5" stroke="#0f0f0f" stroke-width="1.6" fill="none"/></svg></span><div><b>Make a Quote</b><br>hello@gullwindstonecut.au</div></div>
  </div>
  <div class="newsletter"><h5>Newsletter</h5><div class="nl-input"><span>Enter your email</span><i></i></div></div>
  <div class="socials"><i></i><i></i><i></i></div>
  <div class="f-rule"></div>
  <p class="copyright">© 2026 Copyright Gullwind Stonecut Earthworks. All Rights Reserved</p>
</footer>

</body>
</html>
```